Web Design Project

We need a web design for a new company that we started called TALMO CNG. TALMO CNG is a company that will build, own and operate compressed natural gas fueling stations throughout the United States. Our primary customers are Trucking companies and the stations will be built for semi trucks. CNG is better for the environment than diesel fuel, and will save trucking companies loads of money. It is also a domestic product which means that it will create American jobs and help America become energy independent. I have attached a logo that we are using. We dont need to stay with this logo persay, but it is what we have for now. We have a video on Youtube that shows a bit of what we are doing. just search for TALMO CNG. TALMO CNG is a sister company of Haulbright of Arizona,www.hbrtqx.example and a nationwide distributor of VANTO RIG, www.vantorig.example. We will need links to these sites. Please make any pictures of trucks Haulbright trucks, and please do not use pictures of cabover trucks.

Target Market(s)

The target market are truck drivers and truckers.

Industry/Entity Type

Environment

Requirements
Must have
• Map showing station locations, a page with industry news, a page with a savings calculator (we can code the calculator) Site should have links to

```html
<!DOCTYPE html>
<html lang="en">
<head>
<meta charset="utf-8">
<title>TALMO CNG</title>
<link rel="stylesheet" href="https://fonts.googleapis.com/css2?family=Oswald:wght@400;500&family=PT+Sans:ital,wght@0,400;0,700;1,400&display=swap">
<style>
:root{
  --page:#ececec;
  --panel:#ffffff;
  --green:#2b8a2f;
  --green-dark:#1c6a23;
  --green-light:#4cbf4a;
  --logo:#3fc53a;
  --yellow:#f3e55a;
  --ink:#333333;
  --body:#666666;
  --head-gray:#454545;
  --rule:#dddddd;
}
*{margin:0;padding:0;box-sizing:border-box}
html,body{width:872px;height:1200px;overflow:hidden}
body{background:var(--page);font-family:"PT Sans",sans-serif;color:var(--body);position:relative}
.sheet{position:absolute;left:24px;top:8px;width:822px;height:1110px;background:var(--panel);border-radius:14px}
.abs{position:absolute}
.toplinks{right:38px;top:19px;font-size:9.5px;color:#777}
.toplinks span{margin:0 5px;color:#aaa}
.brand{left:55px;top:38px;font-family:"Oswald",sans-serif;font-weight:500;font-size:36px;color:var(--logo);letter-spacing:1px;display:flex;align-items:center;gap:8px}
.brand i{display:inline-block;width:14px;height:14px;background:var(--logo);border-radius:50%}
.callout{right:49px;top:52px;text-align:right;font-family:"Oswald",sans-serif;color:var(--green)}
.callout .lbl{font-size:11.5px}
.callout .num{font-size:25px;font-weight:500;color:var(--green-dark);line-height:1.1}
.nav{left:39px;top:105px;width:798px;height:42px;border-radius:4px;background:linear-gradient(#5ccb57,#2f9a33 55%,#258a2a);display:flex;align-items:center}
.nav a{font-family:"Oswald",sans-serif;color:#fff;font-size:12.5px;text-decoration:none;text-align:center;border-right:1px solid rgba(255,255,255,.35);line-height:18px}
.nav a:last-child{border-right:none}
.hero{left:39px;top:151px;width:798px;height:287px;background:var(--green);border-radius:3px}
.photo{left:9px;top:8px;width:543px;height:267px;background:linear-gradient(180deg,#4b4b4b 0%,#e9e6c8 40%,#ece85a 60%,#d9d9d9 85%,#6a6a6a 100%)}
.dotsbar{left:9px;top:256px;width:543px;height:19px;background:rgba(0,0,0,.45);display:flex;justify-content:center;align-items:center;gap:3px}
.dotsbar b{width:5px;height:5px;border-radius:50%;background:#bbb}
.dotsbar b:first-child{background:#fff}
.map{left:560px;top:8px;width:228px;height:224px;background:linear-gradient(135deg,#eedc9a,#e9d48a 50%,#bcd6ee)}
.mapbar{left:560px;top:232px;width:228px;height:43px;background:var(--green-dark);display:flex;align-items:center;justify-content:space-between;padding:0 10px 0 18px}
.mapbar h3{font-family:"Oswald",sans-serif;font-weight:400;color:#fff;font-size:15px}
.mapbar a{font-size:9px;color:#fff;background:var(--green-light);border-radius:3px;padding:3px 9px;text-decoration:none}
.welcome{left:46px;top:462px;width:533px}
.welcome h1{font-family:"PT Sans",sans-serif;font-weight:400;color:var(--green);font-size:17px;margin-bottom:9px}
.welcome p{font-size:10px;line-height:17px;margin-bottom:8px}
.welcome p.lead{color:var(--ink);font-weight:700;margin-bottom:9px}
.feature{width:249px}
.feature .banner{display:flex;height:88px}
.feature .tag{width:94px;background:var(--green-dark);display:flex;align-items:center;justify-content:center;text-align:center;font-family:"Oswald",sans-serif;color:var(--yellow);font-size:15.5px;line-height:20px}
.feature .img{flex:1}
.feature h4{font-weight:400;color:var(--ink);font-size:10.5px;margin:12px 2px 3px}
.feature p{font-size:7.9px;line-height:13.6px;margin:0 2px}
.feature a{display:inline-block;font-size:8.5px;color:var(--ink);text-decoration:none;margin:4px 2px 0}
.box{width:232px;background:#fff;border:1px solid var(--rule);border-radius:4px;overflow:hidden;box-shadow:0 0 3px rgba(0,0,0,.08)}
.box .hd{background:var(--head-gray);color:#fff;font-size:14.5px;padding:0 22px;height:38px;line-height:40px}
.calc{left:605px;top:455px;height:282px}
.calc .device{margin:11px auto 0;width:161px;height:226px;border-radius:16px;background:linear-gradient(#f7e06a,#f4cf2b 50%,#f0a92a)}
.quotes{left:605px;top:753px;height:338px}
.quotes .bd{padding:17px 20px 0 22px}
.quotes p{font-style:italic;font-size:9.2px;line-height:16px}
.quotes .by{font-style:normal;font-weight:700;color:var(--ink);font-size:9px;margin:9px 0 14px}
.footnav{left:34px;top:1133px;font-size:9.8px;color:#222}
.footnav span{margin:0 6px;color:#555}
.copy{left:34px;top:1158px;font-size:8.8px;color:#777}
.touch{left:671px;top:1133px;font-size:8.8px;color:#666;display:flex;align-items:center;gap:4px}
.touch .lbl{margin-right:4px}
.touch i{width:21px;height:21px;border-radius:50%;background:#111;display:inline-block}
</style>
</head>
<body>
<div class="sheet"></div>

<div class="abs toplinks">Customer Services<span>|</span>FAQ<span>|</span>Support<span>|</span>Member</div>
<div class="abs brand"><i></i>TALMO CNG</div>
<div class="abs callout"><div class="lbl">CALL US NOW FOR CNG</div><div class="num">555.014.2290</div></div>

<nav class="abs nav">
  <a style="width:84px">HOME</a><a style="width:90px">ABOUT US</a><a style="width:84px">SERVICES</a><a style="width:126px">WHY CHOOSE CNG</a><a style="width:97px">LOCATIONS</a><a style="width:112px">LATEST NEWS</a><a style="width:107px">TESTIMONIALS</a><a style="width:98px">CONTACT</a>
</nav>

<section class="abs hero">
  <div class="abs photo" role="img" aria-label="Photo of yellow CNG fuel tanks mounted in the rear of a white vehicle"></div>
  <div class="abs dotsbar"><b></b><b></b><b></b><b></b></div>
  <div class="abs map" role="img" aria-label="Map of the eastern United States showing CNG service area"></div>
  <div class="abs mapbar"><h3>CNG Provides Area Map</h3><a href="#">view full</a></div>
</section>

<section class="abs welcome">
  <h1>Welcome to TALMO CNG Website Mainpage..</h1>
  <p class="lead">Lorem ipsum dolor sit amet, consectetuer adipiscing elit. Nam cursus. Morbi ut mi. Nullam enim leo, egestas id, condimentum at, laoreet mattis, massa. Sed eleifend nonummy diam.</p>
  <p>Praesent mauris ante, elementum et, bibendum at, posuere sit amet, nibh. Duis tincidunt lectus quis dui viverra vestibulum. Suspendisse vulputate aliquam dui. Nulla elementum dui ut augue. Aliquam vehicula mi at mauris. Maecenas placerat, nisl at consequat rhoncus, sem nunc gravida justo, quis eleifend arcu velit quis lacus. Morbi magna magna, tincidunt a, mattis non, imperdiet vitae, tellus. Sed odio est, auctor ac, sollicitudin in, consequat vitae, orci. Fusce id felis.</p>
  <p>Mauris vel lacus vitae felis vestibulum volutpat. Etiam est nunc, venenatis in, tristique eu, imperdiet ac, nisl. Cum sociis natoque penatibus et magnis dis parturient montes, nascetur ridiculus mus. In iaculis facilisis massa. Etiam eu urna. Sed porta. Suspendisse quam leo, molestie sed, luctus quis, feugiat in, pede. Fusce tellus. Sed metus augue, convallis et, vehicula ut, pulvinar eu, ante. Integer orci tellus, tristique vitae, consequat nec, porta vel, lectus. Nulla sit amet diam. Duis non nunc.v</p>
</section>

<article class="abs feature" style="left:47px;top:718px">
  <div class="banner"><div class="tag">FEATURED<br>SERVICES</div><div class="img" role="img" aria-label="Photo of CNG tanks on a truck chassis" style="background:linear-gradient(135deg,#d8d8d8,#8a8a8a)"></div></div>
  <h4>Donec convallis pede</h4>
  <p>Pellentesque habitant morbi tristique senectus et netus et malesuada fames ac turpis egestas. In posuere felis nec tortor. Pellentesque faucibus. Ut accumsan ultricies elit.</p>
  <a href="#">Read more &#9656;</a>
</article>
<article class="abs feature" style="left:319px;top:718px">
  <div class="banner"><div class="tag">CNG<br>BENEFITS</div><div class="img" role="img" aria-label="Photo of a worker refueling a green truck with CNG" style="background:linear-gradient(135deg,#3f7a3a,#2a3a2c)"></div></div>
  <h4>Donec convallis pede</h4>
  <p>Pellentesque habitant morbi tristique senectus et netus et malesuada fames ac turpis egestas. In posuere felis nec tortor. Pellentesque faucibus. Ut accumsan ultricies elit.</p>
  <a href="#">Read more &#9656;</a>
</article>
<article class="abs feature" style="left:44px;top:916px">
  <div class="banner"><div class="tag">POWER<br>SAVING</div><div class="img" role="img" aria-label="Photo of solar panels under a blue sky" style="background:linear-gradient(160deg,#5fa3e0,#1d4a9a)"></div></div>
  <h4>Donec convallis pede</h4>
  <p>Pellentesque habitant morbi tristique senectus et netus et malesuada fames ac turpis egestas. In posuere felis nec tortor. Pellentesque faucibus. Ut accumsan ultricies elit.</p>
  <a href="#">Read more &#9656;</a>
</article>
<article class="abs feature" style="left:316px;top:916px">
  <div class="banner"><div class="tag">SAVE<br>YOUR MONEY</div><div class="img" role="img" aria-label="Photo of a surprised man holding banknotes" style="background:linear-gradient(135deg,#f4f4f4,#7fb2de)"></div></div>
  <h4>Donec convallis pede</h4>
  <p>Pellentesque habitant morbi tristique senectus et netus et malesuada fames ac turpis egestas. In posuere felis nec tortor. Pellentesque faucibus. Ut accumsan ultricies elit.</p>
  <a href="#">Read more &#9656;</a>
</article>

<aside class="abs box calc">
  <div class="hd">Money Saving Calculator</div>
  <div class="device" role="img" aria-label="Illustration of a yellow pocket calculator"></div>
</aside>

<aside class="abs box quotes">
  <div class="hd">What Our Customer Says</div>
  <div class="bd">
    <p>Pellentesque faucibus. Ut accumsan ultricieas elit. Maecenas at justo id velit placerat molestie. Donec dictum lectus non odio. Cras a ante vitae enim iaculis aliquam. Mauris nunc quam, venenatis nec, euismod sit amet</p>
    <p class="by">By Author Name</p>
    <p>Mauris vel lacus vitae felis vestibulum volutpat. Etiam est nunc, venenatis in, tristique eu, imperdiet ac, nisl. Cum sociis natoque penatibus et magnis dis parturient montes, nascetur ridiculus mus. In iaculis facilisis massa. Etiam eu urna. Sed porta. Suspendisse quam leo, molestie sed, luctus quis, feugiat in</p>
    <p class="by">By Author Name</p>
  </div>
</aside>

<footer>
  <div class="abs footnav">HOME<span>|</span>ABOUT US<span>|</span>SERVICES<span>|</span>WHY CHOOSE CNG<span>|</span>LOCATIONS<span>|</span>LATEST NEWS<span>|</span>TESTIMONIALS<span>|</span>CONTACT</div>
  <div class="abs copy">Copyright &copy; 2012 Company Name.&nbsp; All right reserved.&nbsp; Term of Use</div>
  <div class="abs touch"><span class="lbl">Get In Touch With Us</span><i></i><i></i><i></i></div>
</footer>
</body>
</html>
```